Social Media Graphics - Copperfield Loop

Create 6-7 individual social media graphics (square size) to encourage folks to join our online course, using either of the text below (only one set of text per graphic:

The Lantern Ridge Method
How to Create a 7-Figure Business From Scratch
Sign Up Today!

Or

The Lantern Ridge Method
Fast-track Your Way to a Multi-Million Business!
Sign Up Today!

For the color scheme of the graphics, use 1 or 2 colors in the color palette attached; or use any colors that look nice with their outfits; AVOID using red, white and blue altogether because it will look like an Independence Day (4th of July) graphic and we don’t want that; make sure the graphics appeal to both men and women

Make sure each graphic contains 1 of the 2 pics attached; and make sure one of the graphics is all TEXT only.

Target Market(s)

men and women looking to make more money

Industry/Entity Type

entrepreneurship

Requirements
Must have
• see the text document attached
Nice to have
• We are open to a nice color design; the color palette colors are not required, especially we don't want red, white and blue used together
Should not have
• AVOID using red, white and blue altogether because it will look like an Independence Day (4th of July) graphic and we dont want that

```html
<!DOCTYPE html>
<html lang="en">
<head>
<meta charset="utf-8">
<title>Copperfield Loop — The Lantern Ridge Method social set</title>
<link rel="stylesheet" href="https://fonts.googleapis.com/css2?family=Montserrat:wght@300;400;700;800&display=swap">
<style>
  :root{
    --sheet:#ffffff;
    --ink:#0c0c1a;
    --white:#ffffff;
    --plum:#3b0a57;
    --plum-deep:#2a0740;
    --blush:#fbb3c4;
    --violet:#6a1bb0;
    --violet-soft:#8a3fd0;
    --peach:#fcdad6;
    --onyx:#121212;
    --cyan:#00f8fa;
    --magenta:#e800d8;
    --orchid:#f39bd8;
    --dress:#e8265a;
    --shirt:#141414;
  }
  *{box-sizing:border-box;margin:0;padding:0}
  html,body{width:1200px;height:797px;overflow:hidden;background:var(--sheet)}
  body{font-family:"Montserrat",sans-serif;position:relative}
  .tile{position:absolute;width:389px;height:389px;overflow:hidden}
  .tile--r1{top:0}.tile--r2{top:398px}
  .tile--c1{left:0}.tile--c2{left:398px}.tile--c3{left:797px}
  .decor{position:absolute;inset:0;width:389px;height:389px}
  .headline{position:absolute;top:19px;left:16px;right:16px;text-transform:uppercase;line-height:1.18;font-size:16.5px;letter-spacing:-.1px}
  .headline--center{text-align:center}
  .headline .title{display:block;font-weight:800}
  .headline .line{display:block;font-weight:300}
  .headline b{font-weight:800}
  .cta{position:absolute;top:93px;left:16px;width:131px;height:27px;border-radius:9px;font-weight:800;font-size:11.5px;line-height:27px;text-align:center;text-transform:uppercase}
  .cta--center{left:129px}
  .hosts{position:absolute;bottom:0;height:268px;border-radius:120px 120px 0 0;background:linear-gradient(90deg,var(--dress) 0%,var(--dress) 50%,var(--shirt) 52%,var(--shirt) 100%)}

  .tile--blush{background:var(--blush);color:var(--ink)}
  .tile--blush .cta{background:var(--plum);color:var(--white)}
  .tile--violet{background:var(--violet);color:var(--white)}
  .tile--violet .cta{background:var(--white);color:var(--violet)}
  .tile--peach{background:var(--peach);color:var(--ink)}
  .tile--peach .cta{background:var(--plum);color:var(--white)}
  .tile--onyx{background:var(--onyx);color:var(--white)}
  .tile--onyx .headline{top:122px;font-size:21px;line-height:1.25}
  .tile--onyx .cta{top:236px;background:var(--cyan);color:var(--onyx)}
  .tile--plum{background:var(--plum-deep);color:var(--white)}
  .tile--plum .cta{background:var(--orchid);color:var(--plum-deep)}
  .tile--cyan{background:var(--cyan);color:var(--ink)}
  .tile--cyan .cta{background:#000;color:var(--cyan)}
</style>
</head>
<body>

<section class="tile tile--r1 tile--c1 tile--blush">
  <svg class="decor" viewBox="0 0 389 389">
    <defs><linearGradient id="ringFade" x1="0" x2="1"><stop offset="0" stop-color="#e800d8"/><stop offset=".5" stop-color="#8a2cf2"/><stop offset="1" stop-color="#3b0a57"/></linearGradient></defs>
    <circle cx="195" cy="355" r="162" fill="none" stroke="url(#ringFade)" stroke-width="36"/>
  </svg>
  <div class="hosts" role="img" aria-label="Photo of the two course hosts, a woman in a pink dress and a man in black, arms crossed and smiling" style="left:81px;width:234px"></div>
  <h2 class="headline headline--center"><span class="title">The Lantern Ridge Method:</span><span class="line">How to create a <b>7-figure</b></span><span class="line"><b>business</b> from <b>scratch</b></span></h2>
  <div class="cta cta--center">Sign up today!</div>
</section>

<section class="tile tile--r1 tile--c2 tile--violet">
  <svg class="decor" viewBox="0 0 389 389">
    <path d="M0 262 C60 300 120 290 170 250 C230 200 300 130 389 170 L389 389 L0 389 Z" fill="var(--violet-soft)" opacity=".85"/>
  </svg>
  <div class="hosts" role="img" aria-label="Photo of the two course hosts, a woman in a pink dress and a man in black, arms crossed and smiling" style="left:130px;width:259px"></div>
  <h2 class="headline"><span class="title">The Lantern Ridge Method:</span><span class="line">Fast-track your way to a</span><span class="line"><b>multi-million business!</b></span></h2>
  <div class="cta">Sign up today!</div>
</section>

<section class="tile tile--r1 tile--c3 tile--peach">
  <svg class="decor" viewBox="0 0 389 389">
    <path d="M389 104 C300 90 250 150 240 220 C230 280 70 290 70 389 L389 389 Z" fill="#fdf3f3"/>
  </svg>
  <div class="hosts" role="img" aria-label="Photo of the two course hosts, a woman in a pink dress and a man in black, arms crossed and smiling" style="left:147px;width:242px"></div>
  <h2 class="headline"><span class="title">The Lantern Ridge Method:</span><span class="line">How to create a <b>7-figure</b></span><span class="line"><b>business</b> from <b>scratch</b></span></h2>
  <div class="cta">Sign up today!</div>
</section>

<section class="tile tile--r2 tile--c1 tile--onyx">
  <svg class="decor" viewBox="0 0 389 389" fill="none" stroke="#6a1bb0" stroke-width="20" stroke-linecap="square">
    <path d="M0 300 L60 360"/><path d="M389 300 L329 360"/>
  </svg>
  <h2 class="headline headline--center"><span class="title">The Lantern Ridge Method:</span><span class="line">Fast-track your way to a</span><span class="line"><b>multi-million business!</b></span></h2>
  <div class="cta cta--center">Sign up today!</div>
</section>

<section class="tile tile--r2 tile--c2 tile--plum">
  <svg class="decor" viewBox="0 0 389 389">
    <path d="M0 280 C80 200 140 180 200 190 C270 200 330 220 389 270 L389 300 C320 260 260 240 200 235 C130 230 70 270 0 330 Z" fill="#f39bd8" opacity=".4"/>
    <path d="M48 152 L110 200" stroke="#f39bd8" stroke-width="4" stroke-linecap="round"/>
  </svg>
  <div class="hosts" role="img" aria-label="Photo of the two course hosts, a woman in a pink dress and a man in black, arms crossed and smiling" style="left:79px;width:254px"></div>
  <h2 class="headline headline--center"><span class="title">The Lantern Ridge Method:</span><span class="line">How to create a <b>7-figure</b></span><span class="line"><b>business</b> from <b>scratch</b></span></h2>
  <div class="cta cta--center">Sign up today!</div>
</section>

<section class="tile tile--r2 tile--c3 tile--cyan">
  <svg class="decor" viewBox="0 0 389 389">
    <defs><linearGradient id="diamondEdge" x1="0" y1="1" x2="1" y2="0"><stop offset="0" stop-color="#e800d8"/><stop offset="1" stop-color="#8a2cf2"/></linearGradient></defs>
    <path d="M365 72 L389 96 M365 72 L66 372 L95 389" fill="none" stroke="url(#diamondEdge)" stroke-width="7"/>
    <path d="M330 140 L389 200 L389 250 L300 160 Z" fill="#8a2cf2" opacity=".8"/>
  </svg>
  <div class="hosts" role="img" aria-label="Photo of the two course hosts, a woman in a pink dress and a man in black, arms crossed and smiling" style="left:123px;width:264px"></div>
  <h2 class="headline"><span class="title">The Lantern Ridge Method:</span><span class="line">Fast-track your way to a</span><span class="line"><b>multi-million business!</b></span></h2>
  <div class="cta">Sign up today!</div>
</section>

</body>
</html>
```